High-end Investment firm website

It needs to feel very high-end. We like clean design which incorporates a good deal of white space with the use of imagery to be provided.

Here are a few examples of design which is appealing:
https://www.brindlecrestcapital.example
https://www.larkmoorgroup.example

Please use the following shade of blue in the design #7BAFD4.

Additional brand colors black, grey and white.

This quorvex doc has a link to all of the content for the site. It also has detailed design notes per section.

https://files.quorvexdocs.example/document/d/7TRQ2WpeLmnb8cvdKa3HJ0XsNf5ZgR1YtUoC9eV4qAs/edit?usp=sharing

Target Market(s)

Investors and companies in our target industries

Industry/Entity Type

Investment

Coding

Coded - Design and coding required

Number of Pages Required

5+ page

Font styles to use
Sans Serif

Requirements
Must have
• Clean feel, lots of white space.
Nice to have
• Clean graphics similar to https://www.brindlecrestcapital.example

```html
<!DOCTYPE html>
<html lang="en">
<head>
<meta charset="utf-8">
<title>Meridane Holdings</title>
<link rel="stylesheet" href="https://fonts.googleapis.com/css2?family=Cormorant+SC:wght@500&family=Libre+Caslon+Text:wght@400;700&family=Karla:wght@400;500;700&display=swap">
<style>
:root{
  --blue:#7BAFD4;
  --blue-deep:#5d93bd;
  --ink:#1c1c1c;
  --text:#2f2f2f;
  --grey:#8a8a8a;
  --pale:#f7f8fa;
  --line:#dfe6ec;
  --white:#ffffff;
  --footer:#1f1f20;
}
*{box-sizing:border-box;margin:0;padding:0}
html,body{width:1200px;height:4255px;overflow:hidden}
body{position:relative;background:var(--white);font-family:"Karla",sans-serif;color:var(--text)}
.abs{position:absolute}
section{position:absolute;left:0;width:1200px}
.eyebrow{position:absolute;font-family:"Karla",sans-serif;font-size:13px;letter-spacing:.6px;text-transform:uppercase;color:var(--blue);font-weight:500}
.heading{position:absolute;font-family:"Libre Caslon Text",serif;font-size:28px;font-weight:700;color:var(--ink)}
.center{left:0;width:1200px;text-align:center}
.rule{position:absolute;left:562px;width:76px;height:2px;background:var(--blue)}
.copy{position:absolute;font-size:16px;line-height:23px;color:var(--text)}
.btn{position:absolute;border:2px solid var(--blue);color:var(--blue);font-size:13px;letter-spacing:1px;text-transform:uppercase;display:flex;align-items:center;justify-content:center;font-weight:500;background:transparent}
.photo{position:absolute}
.marker{position:absolute;width:2px;background:var(--blue)}
.marker::after{content:"";position:absolute;left:-6px;bottom:-10px;border-left:7px solid transparent;border-right:7px solid transparent;border-bottom:11px solid var(--blue)}
/* hero */
.hero{top:0;height:637px;background:linear-gradient(100deg,#f4f5f7 0%,#e9ecef 35%,#c9ced3 55%,#dfe3e7 75%,#b8bdc2 100%)}
.brand{position:absolute;left:78px;top:58px;display:flex;align-items:center;gap:10px;font-family:"Libre Caslon Text",serif;font-size:22px;color:#1b2a3a}
.brand i{width:14px;height:14px;background:var(--blue);display:block}
.nav{position:absolute;top:65px;left:582px;display:flex;gap:0;font-family:"Libre Caslon Text",serif;font-size:11.5px;text-transform:uppercase;color:#111}
.nav a{padding:10px 15px;color:inherit;text-decoration:none}
.nav a.active{background:#545a60;color:var(--white)}
.hero-title{position:absolute;left:79px;top:318px;font-family:"Cormorant SC",serif;font-weight:500;font-size:42px;line-height:41px;letter-spacing:2px;color:#2a2a2a}
/* focus cards */
.focus{top:1162px;height:574px;background:var(--pale)}
.card{position:absolute;top:200px;width:194px;height:279px;background:#fbfbfc;padding:0 20px}
.card.active{background:var(--white);box-shadow:0 4px 18px rgba(0,0,0,.06)}
.card svg{position:absolute;top:24px;left:68px}
.card h3{position:absolute;top:110px;left:20px;right:12px;font-size:16px;font-weight:500;color:var(--blue);line-height:19px;letter-spacing:.3px}
.card.active h3{color:var(--ink)}
.card p{position:absolute;top:160px;left:20px;right:14px;font-size:14px;line-height:18.5px;color:var(--text)}
/* experience */
.experience{top:2262px;height:441px;background:var(--pale)}
.partner{position:absolute;top:262px;width:158px;height:85px;background:var(--white);display:flex;align-items:center;justify-content:center;font-size:20px;font-weight:700;color:#4c6a86;letter-spacing:.5px}
/* team */
.member{position:absolute;top:2904px;width:345px;height:344px}
.member .name{position:absolute;left:0;right:0;bottom:54px;text-align:center;font-family:"Libre Caslon Text",serif;font-size:22px;color:var(--white);font-weight:700}
.member .role{position:absolute;left:0;right:0;bottom:34px;text-align:center;font-size:15px;color:var(--white)}
.member.open{background:rgba(123,175,212,.82)}
.member.open .name{top:38px;bottom:auto}
.member.open p{position:absolute;left:25px;right:25px;top:100px;font-size:14.5px;line-height:20px;color:var(--white)}
.member.open .btn{left:22px;top:240px;width:166px;height:42px;border-color:var(--white);color:var(--white)}
/* contact */
.field{position:absolute;border:1.5px solid var(--blue);background:var(--white);font-size:15px;color:var(--text);padding:12px 13px}
/* footer */
.footer{top:3868px;height:387px;background:var(--footer);color:#d9d9d9}
.fcol{position:absolute;top:58px}
.fcol h4{font-size:12px;font-weight:700;color:var(--blue);letter-spacing:.5px;text-transform:uppercase;padding-bottom:8px;border-bottom:1px solid #444;width:185px;margin-bottom:12px}
.fcol li{list-style:none;font-size:11.5px;line-height:16.5px}
.contact-row{display:flex;gap:10px;font-size:11.5px;line-height:16.5px;margin-bottom:22px}
.signup{display:flex;width:152px;height:28px;margin-top:2px}
.signup span{flex:1;border:1px solid #888;background:#111;font-size:11px;padding:6px 8px;color:#eee}
.signup b{width:28px;background:var(--white);color:#111;display:flex;align-items:center;justify-content:center}
.social{position:absolute;left:314px;top:4160px;display:flex;gap:14px}
.social i{width:12px;height:12px;border-radius:50%;border:1.5px solid #aaa;display:block}
.legal{position:absolute;right:160px;text-align:right;font-size:10px;letter-spacing:.4px;text-transform:uppercase;color:#8f8f8f}
</style>
</head>
<body>

<section class="hero">
  <div class="photo" role="img" aria-label="Two businessmen reviewing documents in a bright office" style="inset:0;background:linear-gradient(100deg,rgba(255,255,255,.55) 0%,rgba(255,255,255,0) 55%)"></div>
  <div class="brand"><i></i>Meridane Holdings</div>
  <nav class="nav">
    <a class="active">Home</a><a>About Us</a><a>Investment Focus</a><a>Industry Focus</a><a>Contact</a>
  </nav>
  <h1 class="hero-title">Partnering with<br>Exceptional Leaders Building<br>World-Class Companies</h1>
</section>

<section class="about" style="top:637px;height:525px">
  <div class="photo" role="img" aria-label="Hand drawing a rising growth chart on a glass screen" style="left:0;top:0;width:600px;height:525px;background:linear-gradient(135deg,#3c5a73 0%,#6e93ae 40%,#b9d0df 70%,#e4eef4 100%)"></div>
  <div class="eyebrow" style="left:678px;top:98px">Rapid growth and profit improvement</div>
  <div class="heading" style="left:677px;top:120px">About Meridane Holdings</div>
  <p class="copy" style="left:677px;top:198px;width:435px">Meridane Holdings focuses on opportunities where it can support senior management to drive rapid growth and profit improvement through capital infusion, technology innovation and organizational expertise. &nbsp;We invest across a variety of growth industries with an emphasis on reshoring and rebuilding America.</p>
  <div class="btn" style="left:678px;top:383px;width:167px;height:50px">Learn More</div>
</section>
<div class="marker" style="left:683px;top:637px;height:40px"></div>

<section class="focus">
  <div class="eyebrow center" style="top:98px">What we do</div>
  <div class="heading center" style="top:120px">Area of Focus</div>

  <div class="card" style="left:76px">
    <svg width="58" height="62" viewBox="0 0 58 62" fill="none" stroke="#7BAFD4" stroke-width="3"><path d="M29 3 L53 12 V30 C53 45 42 55 29 59 C16 55 5 45 5 30 V12 Z"/><path d="M29 20 l4 9 h9 l-7 6 3 9 -9-6 -9 6 3-9 -7-6 h9 z" fill="#7BAFD4" stroke="none"/></svg>
    <h3>Defense</h3>
    <p>Lorem ipsum dolor sit amet, consectetur adi piscing elit, sed do ei usmod tempor incidi dunt ut labore et.</p>
  </div>
  <div class="card" style="left:290px">
    <svg width="60" height="50" viewBox="0 0 60 50" fill="none" stroke="#7BAFD4" stroke-width="2.5"><rect x="3" y="3" width="54" height="44"/><line x1="3" y1="12" x2="57" y2="12"/><rect x="24" y="30" width="12" height="11"/><path d="M26 30 v-4 a4 4 0 0 1 8 0 v4"/><line x1="12" y1="21" x2="48" y2="21"/></svg>
    <h3>Cybersecurity</h3>
    <p>Lorem ipsum dolor sit amet, consectetur adi piscing elit, sed do ei usmod tempor incidi dunt ut labore et.</p>
  </div>
  <div class="card active" style="left:504px">
    <svg width="60" height="60" viewBox="0 0 60 60" fill="none" stroke="#1c1c1c" stroke-width="2.5"><rect x="22" y="4" width="16" height="36" rx="8"/><rect x="6" y="30" width="14" height="20"/><rect x="40" y="30" width="14" height="20"/><line x1="2" y1="56" x2="58" y2="56"/><line x1="30" y1="40" x2="30" y2="56"/></svg>
    <h3>Industrials</h3>
    <p>Lorem ipsum dolor sit amet, consectetur adi piscing elit, sed do ei usmod tempor incidi dunt ut labore et.</p>
  </div>
  <div class="card" style="left:718px">
    <svg width="54" height="50" viewBox="0 0 54 50" fill="none" stroke="#7BAFD4" stroke-width="2.5"><rect x="3" y="3" width="44" height="36"/><line x1="10" y1="13" x2="40" y2="13"/><line x1="10" y1="21" x2="40" y2="21"/><line x1="10" y1="29" x2="30" y2="29"/><path d="M38 30 l12 12 -4 4 -12-12z"/></svg>
    <h3>Digital Enterprise</h3>
    <p>Lorem ipsum dolor sit amet, consectetur adi piscing elit, sed do ei usmod tempor incidi dunt ut labore et.</p>
  </div>
  <div class="card" style="left:932px">
    <svg width="56" height="50" viewBox="0 0 56 50" fill="none" stroke="#7BAFD4" stroke-width="2.5"><rect x="3" y="3" width="50" height="34"/><line x1="28" y1="37" x2="28" y2="46"/><line x1="16" y1="47" x2="40" y2="47"/><path d="M10 22 q6-8 12 0 t12 0 t12 0"/></svg>
    <h3>Technology and Professional</h3>
    <p>Lorem ipsum dolor sit amet, consectetur adi piscing elit, sed do ei usmod tempor incidi dunt ut labore et.</p>
  </div>
</section>
<div class="marker" style="left:680px;top:1162px;height:0"></div>

<section class="invest" style="top:1736px;height:526px">
  <div class="eyebrow" style="left:78px;top:139px">Long term growth &amp; revenue generation</div>
  <div class="heading" style="left:77px;top:161px">Investment Focus</div>
  <p class="copy" style="left:77px;top:235px;width:415px">We place capital for long-term growth and revenue generation. Our investment horizon enables a focus on building strong sustainable companies, with empowered teams maximizing impact.</p>
  <div class="btn" style="left:78px;top:348px;width:168px;height:50px">Learn More</div>
  <div class="photo" role="img" aria-label="Businessman on a balcony overlooking a city skyline at sunrise" style="left:600px;top:0;width:600px;height:526px;background:linear-gradient(180deg,#a9b3c4 0%,#c8ccd6 35%,#e7ddd4 52%,#9aa6b6 62%,#d3d8df 100%)"></div>
</section>
<div class="marker" style="left:172px;top:1162px;height:45px"></div>
<div class="marker" style="left:1116px;top:1653px;height:155px"></div>
<div class="marker" style="left:720px;top:2150px;height:157px"></div>

<section class="experience">
  <div class="eyebrow center" style="top:98px">Companies we have invested in</div>
  <div class="heading center" style="top:120px">Investment Experience</div>
  <div class="rule" style="top:160px"></div>
  <p class="copy center" style="top:200px;font-size:15px">The Meridane Holdings team has invested in, managed and served on the boards of a variety of high performing companies.</p>
  <div class="partner" style="left:76px">Tallgrove</div>
  <div class="partner" style="left:253px">Pellora</div>
  <div class="partner" style="left:430px">Ashbourne</div>
  <div class="partner" style="left:607px">Quillpay</div>
  <div class="partner" style="left:784px">Orvanta</div>
  <div class="partner" style="left:961px">Lintera</div>
</section>
<div class="marker" style="left:598px;top:2628px;height:120px"></div>

<div class="eyebrow center" style="top:2800px">Peoples behind</div>
<div class="heading center" style="top:2822px">Management Team</div>
<div class="rule" style="top:2864px"></div>

<div class="member" role="img" aria-label="Portrait of a team member" style="left:-277px;background:#3d4a5a"></div>
<div class="member" role="img" aria-label="Portrait of Harlan Vessey on a blue backdrop" style="left:75px;background:linear-gradient(180deg,#3a4fa8 0%,#5064b5 60%,#2d3550 100%)">
  <div class="name">Harlan Vessey</div><div class="role">Partner at Meridane Holdings</div>
</div>
<div class="member" role="img" aria-label="Portrait of Colin Araby in an office" style="left:427px;background:linear-gradient(180deg,#c9ccd0 0%,#9aa1a8 55%,#2a3140 100%)">
  <div class="name">Colin Araby</div><div class="role">Partner at Meridane Holdings</div>
</div>
<div class="member" role="img" aria-label="Portrait of Nessa Whitcombe" style="left:779px;background:linear-gradient(180deg,#9cbfdb,#7faed3)">
  <div class="member open" style="left:0;top:0">
    <div class="name">Nessa Whitcombe</div>
    <p>Nessa Whitcombe is a Partner at Meridane Holdings, where she sits on the investment committee and works with holding company leadership helping accelerate growth through strategy, systems and team development.</p>
    <div class="btn">Learn More</div>
  </div>
</div>
<div class="member" role="img" aria-label="Portrait of a team member" style="left:1131px;background:#4a5566"></div>

<section class="contact" style="top:3342px;height:526px">
  <div class="photo" role="img" aria-label="Aerial view of a Manhattan skyline under a blue sky" style="left:0;top:0;width:600px;height:526px;background:linear-gradient(180deg,#5d8fd1 0%,#a9c6e6 30%,#c3ccd4 45%,#7b7f86 75%,#3e4146 100%)"></div>
  <div class="eyebrow" style="left:676px;top:100px">Let us give you the solution</div>
  <div class="heading" style="left:676px;top:122px">Contact Us</div>
  <div class="field" style="left:674px;top:199px;width:221px;height:44px">Name</div>
  <div class="field" style="left:906px;top:199px;width:222px;height:44px">Email</div>
  <div class="field" style="left:674px;top:255px;width:454px;height:117px">Message</div>
  <div class="btn" style="left:674px;top:382px;width:167px;height:50px">Learn More</div>
</section>

<section class="footer">
  <div class="fcol" style="left:159px"><h4>Navigation</h4>
    <ul><li>Home</li><li>About Us</li><li>Investment Focus</li><li>Industry Focus</li><li>Contact</li></ul></div>
  <div class="fcol" style="left:344px"><h4>Area of Focus</h4>
    <ul><li>Defense</li><li>Cybersecurity</li><li>Industrials</li><li>Digital Enterprise</li><li>Technology &amp; Professional Services</li></ul></div>
  <div class="fcol" style="left:622px"><h4>Contact</h4>
    <div class="contact-row"><svg width="10" height="14" viewBox="0 0 10 14"><path d="M5 0a5 5 0 0 1 5 5c0 4-5 9-5 9S0 9 0 5a5 5 0 0 1 5-5z" fill="#bbb"/><circle cx="5" cy="5" r="2" fill="#1f1f20"/></svg><div>Meridane Holdings<br>123 Lorem Ipsum Dr<br>New York, NY 10001</div></div>
    <div class="contact-row"><svg width="12" height="12" viewBox="0 0 12 12"><path d="M2 0l3 3-1.5 2a7 7 0 0 0 3.5 3.5L9 7l3 3-2 2C5 12 0 7 0 2z" fill="#bbb"/></svg><div>(555) 014-0394</div></div>
    <div class="contact-row"><svg width="13" height="10" viewBox="0 0 13 10" fill="none" stroke="#bbb"><rect x=".5" y=".5" width="12" height="9"/><path d="M.5 .5l6 5 6-5"/></svg><div>info@meridaneholdings.example</div></div>
  </div>
  <div class="fcol" style="left:889px"><h4 style="border:none">Sign up for the latest</h4>
    <div class="signup"><span>Email Address</span><b>→</b></div></div>

  <div class="brand" style="left:159px;top:272px;font-size:20px;color:var(--blue)"><i></i>Meridane</div>
  <div class="legal" style="top:289px">Privacy Policy &nbsp;|&nbsp; Cookie Policy &nbsp;|&nbsp; Data Usage Policy</div>
  <div class="legal" style="top:308px;color:#b0b0b0">© 2020 Meridane Holdings - All Rights Reserved</div>
</section>
<div class="social"><i></i><i></i><i></i><i></i></div>

</body>
</html>
```